Indoor Air Restoration company needs graphic design for a 6x12 v nose trailer to wrap

We offer mold services, duct cleaning, water damage clean up and odor removal. "We find, fix and prevent mold, odor and allergen problems" is what we want to communicate on this trailer, which is a rolling billboard. We like the blue and orange color themes, as found in our logo. The company name is Bright Nest Partners and the logo is attached below. We'd like to see our message clearly, company name and what we offer. We tend to lean towards white letters on a darker background (blue or orange) but are very open to outside ideas, as we are stuck! Our website is available for reference if that is helpful. www.brightnestpro.com The phone number to be printed on truck is 302-555-0148, Happy designing!!

Target Market(s)

Home owners

Industry/Entity Type

Indoor Air Quality, Mold Remediation

Font styles to use
Sans Serif

Colors
0054AA
0677BA
7BADD7
CADEEF
E8F1F8
F0912C
F2A743
F7CA91
FBE8D2
FDF5EE

Requirements
Must have
• our message, company name and phone
Nice to have
• services we offer (mold remediation, duct cleaning, water damage and odor removal
Should not have
• cartoon feel

```html
<!DOCTYPE html>
<html lang="en">
<head>
<meta charset="utf-8">
<title>Bright Nest Partners – Trailer Wrap</title>
<link rel="stylesheet" href="https://fonts.googleapis.com/css2?family=Roboto+Condensed:wght@700;900&family=Noto+Sans:wght@700&family=Montserrat:wght@800&display=swap">
<style>
  :root {
    --navy: #2e3083;
    --sun-yellow: #f6e620;
    --sun-orange: #f8a51d;
    --white: #ffffff;
    --ink: #231f20;
    --photo-light: #dfe8f2;
    --photo-mid: #8fa6c8;
  }
  * { box-sizing: border-box; margin: 0; padding: 0; }
  html, body { width: 750px; height: 1200px; overflow: hidden; background: var(--white); }
  .canvas { position: relative; width: 750px; height: 1200px; background: var(--white); }

  .wrap-panel {
    position: absolute; left: 105px; top: 60px; width: 540px; height: 1080px;
    background: var(--navy); overflow: hidden; outline: 1px solid var(--ink);
  }
  .header-wave { position: absolute; left: 0; top: 0; width: 540px; height: 380px; }

  .brand-mark {
    position: absolute; left: 0; right: 0; top: 90px;
    display: flex; align-items: center; justify-content: center; gap: 10px;
    font-family: "Roboto Condensed", sans-serif; font-weight: 700;
    font-size: 28px; color: var(--navy); letter-spacing: 0.5px;
  }
  .brand-mark .brand-square { width: 22px; height: 22px; background: var(--navy); }

  .headline {
    position: absolute; left: 0; right: 0; top: 196px; text-align: center;
    font-family: "Roboto Condensed", sans-serif; font-weight: 900;
    color: var(--navy); text-transform: uppercase; line-height: 1;
  }
  .headline .line-main { display: block; font-size: 76px; letter-spacing: -1px; }
  .headline .line-sub { display: block; font-size: 60px; margin-top: 2px; }

  .family-photo {
    position: absolute; left: 0; top: 700px; width: 540px; height: 330px;
    background: linear-gradient(180deg, rgba(46,48,131,0) 0%, var(--photo-mid) 45%, var(--photo-light) 80%, var(--white) 100%);
  }

  .services { position: absolute; left: 26px; top: 400px; color: var(--white); font-family: "Noto Sans", sans-serif; font-weight: 700; }
  .services-title {
    font-size: 50px; letter-spacing: -1.5px; line-height: 1;
    text-decoration: underline; text-decoration-thickness: 4px; text-underline-offset: 6px;
  }
  .service-list { list-style: none; margin-top: 22px; }
  .service-list li { font-size: 54px; letter-spacing: -1.8px; line-height: 69px; white-space: nowrap; }
  .service-list li::before { content: "•"; font-size: 30px; vertical-align: middle; margin-right: 4px; }

  .tagline {
    position: absolute; left: 30px; right: 30px; top: 840px; text-align: center;
    font-family: "Noto Sans", sans-serif; font-weight: 700; font-size: 25px;
    line-height: 1.25; color: var(--navy); letter-spacing: -0.3px;
  }

  .contact-band {
    position: absolute; left: 0; bottom: 0; width: 540px; height: 118px;
    border-radius: 40px 40px 0 0;
    background: linear-gradient(100deg, var(--sun-yellow) 0%, var(--sun-orange) 100%);
    display: flex; align-items: center; padding-left: 40px; gap: 14px;
  }
  .phone-icon { width: 60px; height: 60px; flex: none; }
  .phone-number {
    font-family: "Montserrat", sans-serif; font-weight: 800; font-size: 52px;
    color: var(--ink); letter-spacing: 1px; white-space: nowrap;
  }
</style>
</head>
<body>
<main class="canvas">
  <section class="wrap-panel">
    <svg class="header-wave" viewBox="0 0 540 380" aria-hidden="true">
      <defs>
        <linearGradient id="sunGradient" x1="0" y1="0" x2="0" y2="1">
          <stop offset="0" stop-color="#f6e620"/>
          <stop offset="1" stop-color="#f8a51d"/>
        </linearGradient>
      </defs>
      <path d="M0,0 H540 V305 C470,350 390,368 300,360 C200,350 100,322 0,340 Z" fill="url(#sunGradient)"/>
      <path d="M0,340 C100,322 200,350 300,360 C390,368 470,350 540,305" fill="none" stroke="#f6e620" stroke-width="6"/>
    </svg>

    <div class="brand-mark"><span class="brand-square"></span>Bright Nest Partners</div>

    <h1 class="headline">
      <span class="line-main">Bright Nest</span>
      <span class="line-sub">Partners</span>
    </h1>

    <div class="family-photo" role="img" aria-label="Photo of a smiling family with two young children relaxing on a bed"></div>

    <div class="services">
      <h2 class="services-title">Our services:</h2>
      <ul class="service-list">
        <li>Mold Remediation</li>
        <li>Duct Cleaning</li>
        <li>Water Damage</li>
        <li>Odor Removal</li>
      </ul>
    </div>

    <p class="tagline">We find, fix and prevent mold, odor and allergen problems</p>

    <div class="contact-band">
      <svg class="phone-icon" viewBox="0 0 60 60" aria-hidden="true">
        <defs>
          <linearGradient id="steel" x1="0" y1="0" x2="1" y2="0">
            <stop offset="0" stop-color="#8c8c8c"/>
            <stop offset="0.45" stop-color="#f2f2f2"/>
            <stop offset="1" stop-color="#9a9a9a"/>
          </linearGradient>
        </defs>
        <rect x="1" y="1" width="58" height="58" rx="6" fill="url(#steel)" stroke="#7a7a7a"/>
        <path d="M26,14 c-5,2 -7,8 -7,16 s2,14 7,16 l3,-1 l-1,-9 l-3,0 c-1,-3 -1,-9 0,-12 l3,0 l1,-9 z" fill="#3a3a3a"/>
      </svg>
      <span class="phone-number">302-555-0148</span>
    </div>
  </section>
</main>
</body>
</html>
```